Mobile Landing Page for giveaway Seedbombs done from a institution for handicaped people

We are a social institution that makes seedbombs that contain wildflowers for bees and other insects. During a sutanibel event, these bombs are given to an audience. On the packaging of the seedbombs, there is a QR code that leads to a landing page. We are producing a video showing how our handicapped clients made the seebombs. The Landigpage should look: sustanible, green, and sozial. On the page, there shoud be this Video, a manual how tho use the seedbombs. Something about our work whith the handicapt people a linkt to our Instagram amd a possibility to get involved whith us as well as a donation button. You can find more information about us on: www.talmatte-kollektiv.ch

Target Market(s)

People that are intressetet in envirement and social impakt

Industry/Entity Type

Social Impakt, Urban Gardening

Coding

Coded - Design and coding required

Number of Pages Required

1 page

Font styles to use
Other font styles liked:
• Joanna

Requirements
Must have
• Be optimised for smartphone
Nice to have
• like a floating page, witch leads you throug the different steps, mabey like a plant with ist growing. From the Bombs to the Plan. Or a little game ore something.

```html
<!DOCTYPE html>
<html lang="en">
<head>
<meta charset="utf-8">
<title>Talmatte – Seedbombs</title>
<link href="https://fonts.googleapis.com/css2?family=Gelasio:wght@400;500;600&family=Jost:wght@400;500&display=swap" rel="stylesheet">
<style>
:root{
  --forest:#1f3d31;
  --sage:#b4c1a6;
  --blush:#f8e4dc;
  --terracotta:#d4604f;
  --canvas:#f3f1ec;
  --cream:#f4f1e8;
  --serif:"Gelasio", Georgia, serif;
  --sans:"Jost", Arial, sans-serif;
}
*{box-sizing:border-box;margin:0;padding:0}
html,body{width:1200px;height:2264px;overflow:hidden;background:var(--canvas)}
h1,h2,h3,h4{font-weight:400}
.page{position:absolute;left:174px;top:0;width:852px;height:2264px;overflow:hidden;background:var(--forest);font-family:var(--sans);color:var(--forest)}
.abs{position:absolute}
.btn{position:absolute;display:flex;align-items:center;justify-content:center;gap:6px;font-family:var(--sans);font-size:8px;font-weight:500;letter-spacing:.2px;text-decoration:none}
.btn-light{background:var(--sage);color:var(--forest)}
.btn-dark{background:var(--forest);color:var(--cream)}
.btn-outline{border:1px solid var(--forest);color:var(--forest)}
.photo{position:absolute}

/* background bands */
.blush{position:absolute;left:0;top:1150px;width:852px;height:822px;background:var(--blush);border-radius:0 0 110px 0}
.sage{position:absolute;left:0;top:355px;width:852px;height:892px;background:var(--sage);border-radius:0 0 0 96px}

/* hero */
.hero{position:absolute;left:0;top:0;width:852px;height:355px;background:var(--forest)}
.brand{font-family:var(--serif);font-weight:500;color:var(--cream);letter-spacing:1px;display:flex;align-items:center;gap:6px}
.brand .dot{width:10px;height:10px;border-radius:50%;border:1.5px solid var(--cream)}
.hero .brand{left:75px;top:26px;font-size:16px}
.eyebrow{left:141px;top:116px;font-size:7px;letter-spacing:.6px;color:var(--cream);font-weight:500}
.hero-title{left:141px;top:130px;font-family:var(--serif);font-size:33px;color:var(--cream)}
.hero-text{left:141px;top:194px;width:280px;font-size:10px;line-height:16px;color:var(--cream)}
.hero-photo{left:498px;top:67px;width:354px;height:288px;border-radius:90px 0 70px 0;background:linear-gradient(135deg,#e9e2d4 0%,#b59a74 45%,#6d6b68 70%,#2f4f86 100%)}
.hero-thumb{left:498px;top:355px;width:66px;height:66px;background:linear-gradient(160deg,#a88a62,#5e4a35)}
.donate{left:709px;top:16px;width:66px;height:66px;border-radius:50%;background:var(--terracotta);color:var(--cream);display:flex;align-items:center;justify-content:center;font-size:9px;font-weight:500;letter-spacing:1.2px;text-transform:uppercase}

/* kit */
.kit-box{left:0;top:409px;width:270px;height:240px;background:linear-gradient(120deg,#dfe3dc 0%,#8fa889 40%,#6f8f6c 70%,#dfe3dc 100%)}
.kit-eyebrow{left:324px;top:448px;font-family:var(--serif);font-size:12px}
.kit-title{left:324px;top:468px;font-family:var(--serif);font-size:27px;font-weight:600}
.kit-text{left:324px;top:517px;width:200px;font-size:9px;line-height:15px}
.kit-price{left:324px;top:576px;font-family:var(--serif);font-size:14px;font-weight:600}
.kit-photo{left:582px;top:506px;width:270px;height:223px;border-radius:50px 0 0 0;background:radial-gradient(circle at 45% 50%,#c56a38 0 16%,#f1efe9 17% 100%)}

/* manual */
.section-title{left:0;width:852px;text-align:center;font-family:var(--serif);font-size:26px;line-height:32px}
.section-title b{font-weight:600}
.step{position:absolute;top:871px;width:130px;text-align:center}
.step svg{display:block;margin:0 auto}
.step h3{font-family:var(--serif);font-size:13px;margin-top:14px}
.step p{font-size:8px;line-height:13px;margin-top:10px}

/* video */
.video{left:141px;top:1137px;width:568px;height:222px;background:var(--forest)}
.video-photo{left:434px;top:1137px;width:275px;height:222px;background:linear-gradient(150deg,#5d7a3e,#8a6b4c 60%,#5a4434)}
.video-title{left:177px;top:1185px;font-family:var(--serif);font-size:27px;line-height:32px;color:var(--sage)}
.video-title b{font-weight:600}
.video-text{left:177px;top:1258px;width:210px;font-size:9.5px;line-height:16px;color:var(--sage)}
.play{left:559px;top:1235px;width:24px;height:24px;border-radius:50%;border:1.5px solid var(--cream);display:flex;align-items:center;justify-content:center}

/* instagram */
.insta-title{left:0;top:1412px;width:852px;display:flex;justify-content:center;align-items:center;gap:8px;font-family:var(--serif);font-size:20px;letter-spacing:.5px}
.insta-title .sq{width:14px;height:14px;border:2px solid var(--forest);border-radius:3px}
.grid{left:141px;top:1456px;width:568px;display:grid;grid-template-columns:repeat(4,136px);grid-auto-rows:135px;gap:9px 8px}
.grid div{width:136px;height:135px}

/* newsletter */
.news-box{left:75px;top:1876px;width:702px;height:182px;background:var(--sage);border-radius:96px 0 0 0}
.news-title{left:0;top:1858px;width:852px;text-align:center;font-family:var(--serif);font-size:23px}
.news-title b{font-weight:600}
.news-text{left:0;top:1900px;width:852px;text-align:center;font-size:9px;line-height:15px}
.news-input{left:209px;top:1988px;width:355px;height:18px;border-bottom:1px solid var(--forest);font-family:var(--serif);font-style:italic;font-size:9px;padding:3px 10px}

/* footer */
.footer .brand{left:141px;top:2094px;font-size:22px}
.copy{left:161px;top:2148px;font-size:7px;color:var(--cream)}
.foot-head{top:2102px;font-family:var(--serif);font-size:12px;color:var(--cream)}
.foot-row{display:flex;align-items:center;gap:8px;font-size:8px;line-height:12px;color:var(--cream)}
.social{left:687px;width:22px;height:22px;border-radius:50%;background:var(--cream)}
</style>
</head>
<body>
<main class="page">

  <div class="blush"></div>
  <div class="sage"></div>

  <header class="hero">
    <div class="abs brand"><span class="dot"></span>TALMATTE</div>
    <p class="abs eyebrow">WELCOME TO</p>
    <h1 class="abs hero-title">Talmatte</h1>
    <p class="abs hero-text">A differentiated range of day activities and an individually adapted care setting are aimed at adults of all ages with a mental disability and with physical and psychological impairments.</p>
    <a class="btn btn-light" style="left:141px;top:280px;width:115px;height:25px">Explore seedbombs →</a>
    <div class="photo hero-photo" role="img" aria-label="Photo of two clients working at a wooden craft table in a bright workshop"></div>
    <div class="abs donate">Spenden</div>
  </header>
  <div class="photo hero-thumb" role="img" aria-label="Small photo of wooden craft work"></div>

  <section class="kit">
    <div class="photo kit-box" role="img" aria-label="Photo of the green seedbombs packaging box"></div>
    <p class="abs kit-eyebrow">Love ♥ Gardening?</p>
    <h2 class="abs kit-title">Seedbombs kit</h2>
    <p class="abs kit-text">A differentiated range of day activities and an individually adapted care setting are aimed at adults ...</p>
    <p class="abs kit-price">$199.00</p>
    <a class="btn btn-dark" style="left:324px;top:618px;width:114px;height:25px">Explore seedbombs →</a>
    <a class="btn btn-outline" style="left:443px;top:618px;width:81px;height:25px">Add to cart →</a>
    <div class="photo kit-photo" role="img" aria-label="Photo of seedling pots, soil, seeds and small garden tools"></div>
  </section>

  <section class="manual">
    <h2 class="abs section-title" style="top:776px">Manual how to use the<br><b>seedbombs</b></h2>

    <div class="step" style="left:141px">
      <svg width="74" height="74" viewBox="0 0 74 74" fill="none" stroke="#1f3d31" stroke-width="1.4"><circle cx="37" cy="37" r="35" stroke-opacity=".35"/><path d="M37 2a35 35 0 0 1 35 35"/><circle cx="37" cy="30" r="6"/><path d="M27 44c6 6 14 6 20 0M37 36v10"/></svg>
      <h3>Seeding</h3>
      <p>Lorem ipsum dolor sit amet, consectetur adipiscing elit, sed do eiusmod tempor incididunt.</p>
    </div>
    <div class="step" style="left:287px">
      <svg width="74" height="74" viewBox="0 0 74 74" fill="none" stroke="#1f3d31" stroke-width="1.4"><circle cx="37" cy="37" r="35" stroke-opacity=".35"/><path d="M37 2a35 35 0 0 1 35 35a35 35 0 0 1-35 35"/><path d="M37 22c-7 9-10 14-10 19a10 10 0 0 0 20 0c0-5-3-10-10-19z"/></svg>
      <h3>Waterings</h3>
      <p>Lorem ipsum dolor sit amet, consectetur adipiscing elit, sed do eiusmod tempor incididunt.</p>
    </div>
    <div class="step" style="left:433px">
      <svg width="74" height="74" viewBox="0 0 74 74" fill="none" stroke="#1f3d31" stroke-width="1.4"><circle cx="37" cy="37" r="35" stroke-opacity=".35"/><path d="M37 2a35 35 0 1 1-30 17"/><circle cx="37" cy="37" r="12"/><path d="M37 30v7l5 3"/></svg>
      <h3>Wait a plant</h3>
      <p>Lorem ipsum dolor sit amet, consectetur adipiscing elit, sed do eiusmod tempor incididunt.</p>
    </div>
    <div class="step" style="left:580px">
      <svg width="74" height="74" viewBox="0 0 74 74" fill="none" stroke="#1f3d31" stroke-width="1.4"><circle cx="37" cy="37" r="35"/><path d="M37 52V26M37 36c-8 0-11-5-11-10 6 0 11 3 11 10zM37 32c7 0 10-5 10-9-6 0-10 3-10 9zM28 52h18"/></svg>
      <h3>Grow</h3>
      <p>Lorem ipsum dolor sit amet, consectetur adipiscing elit, sed do eiusmod tempor incididunt.</p>
    </div>
    <a class="btn btn-dark" style="left:380px;top:1058px;width:92px;height:26px">Contact us →</a>
  </section>

  <section class="video-block">
    <div class="abs video"></div>
    <div class="photo video-photo" role="img" aria-label="Video still of two women planting a young seedling in soil"></div>
    <h2 class="abs video-title">How we produce<br><b>Seebombs</b></h2>
    <p class="abs video-text">Lorem Ipsum is simply dummy text of the printing and typesetting industry lorem Ipsum has been the industry's standard dummy text ever since.</p>
    <div class="abs play"><svg width="8" height="9" viewBox="0 0 8 9"><path d="M0 0l8 4.5L0 9z" fill="#f4f1e8"/></svg></div>
  </section>

  <section class="instagram">
    <h2 class="abs insta-title"><span class="sq"></span>TALMATTE</h2>
    <div class="abs grid">
      <div role="img" aria-label="Photo of a client holding yellow flowers" style="background:linear-gradient(160deg,#c9b78f,#b8323a 60%,#e2b21f)"></div>
      <div role="img" aria-label="Photo of clients crafting in a workshop" style="background:linear-gradient(160deg,#8c7b6c,#b54a3a 70%,#d3a07b)"></div>
      <div role="img" aria-label="Photo of dark clay sculptures" style="background:linear-gradient(160deg,#b9b2a6,#3b3530 60%,#1f1c19)"></div>
      <div role="img" aria-label="Photo of a garden with an autumn tree" style="background:linear-gradient(160deg,#6f8fc9,#b8502e 45%,#c9c4b8)"></div>
      <div role="img" aria-label="Photo of clients in a garden in front of a house" style="background:linear-gradient(160deg,#cfd8e0,#5d8a3c 55%,#c9b347)"></div>
      <div role="img" aria-label="Photo of a client having pizza at an outdoor table" style="background:linear-gradient(160deg,#4e7a3a,#b33a35 50%,#e8e0d3)"></div>
      <div role="img" aria-label="Photo of a framed landscape painting" style="background:linear-gradient(160deg,#3b2a1a,#a07a2a 50%,#3b2a1a)"></div>
      <div role="img" aria-label="Photo of two clients reading together" style="background:linear-gradient(160deg,#d6b25a,#c4743f 55%,#e3ddd2)"></div>
    </div>
    <a class="btn btn-outline" style="left:359px;top:1770px;width:133px;height:25px">Follow us on instagram →</a>
  </section>

  <section class="newsletter">
    <div class="abs news-box"></div>
    <h2 class="abs news-title">Subscribe to our <b>newsletter</b></h2>
    <p class="abs news-text">Would you like to stay up to date on what's happening in the Talmatte?<br>Then subscribe to our newsletter:</p>
    <div class="abs news-input">Enter your email address</div>
    <a class="btn btn-outline" style="left:564px;top:1983px;width:80px;height:23px">Subscribe →</a>
  </section>

  <footer class="footer">
    <div class="abs brand"><span class="dot"></span>TALMATTE</div>
    <p class="abs copy">© 2023 <b>Talmatte</b>. All Rights Reserved.</p>

    <h4 class="abs foot-head" style="left:366px">Contact us</h4>
    <div class="abs foot-row" style="left:366px;top:2130px">
      <svg width="8" height="8" viewBox="0 0 10 10"><path d="M2 0l2 3-1 1.5c.8 1.5 1.8 2.5 3.3 3.3L7.8 6.8 10 8.5 8.5 10C4 9.6.4 6 0 1.5z" fill="#f4f1e8"/></svg><span style="font-size:9px;letter-spacing:.5px">0041 61 555 27 14</span>
    </div>
    <div class="abs foot-row" style="left:366px;top:2152px">
      <svg width="8" height="6" viewBox="0 0 10 7"><rect width="10" height="7" fill="#f4f1e8"/><path d="M0 0l5 4 5-4" stroke="#1f3d31" fill="none"/></svg><span style="font-size:7px">info@talmatte-kollektiv.ch</span>
    </div>
    <div class="abs foot-row" style="left:366px;top:2174px;align-items:flex-start">
      <svg width="8" height="10" viewBox="0 0 8 10"><path d="M4 0a4 4 0 0 1 4 4c0 3-4 6-4 6S0 7 0 4a4 4 0 0 1 4-4z" fill="#f4f1e8"/><circle cx="4" cy="4" r="1.4" fill="#1f3d31"/></svg><span style="font-size:7px">Talmatte<br>Talmattweg 14<br>4410 Mattbach</span>
    </div>

    <h4 class="abs foot-head" style="left:525px">Office hours</h4>
    <p class="abs" style="left:525px;top:2128px;font-size:8px;line-height:13px;color:var(--cream)">Monday - Friday<br><span style="font-size:7px">09:00 to 12:00 &amp; 13:00 to 17:00</span></p>
    <a class="btn btn-light" style="left:525px;top:2173px;width:89px;height:25px">Spende jetzt →</a>

    <div class="abs social" style="top:2102px"></div>
    <div class="abs social" style="top:2128px"></div>
  </footer>

</main>
</body>
</html>
```